Brightmere Picture Works LLC
Project: Brightmere Picture Works LLC
Creative Brief
Entertainment
My company is a production company that produces films and music videos in Hollywood California for the festivals and theaters around the world.
I would like something unique and different but can look at the major production company websites such as Kestrel Pics and Meridane for ideas but don't be afraid to go outside the box i want something that stands out and people will remember.
Elegant
Complex
top
i don't like the content or the colors/pics of meridane but i like how they go outside the box i don't want anything simple or normal i life extravagant. This is your chance as a designer and architect to let your creative side out.

```html
<!DOCTYPE html>
<html lang="en">
<head>
<meta charset="utf-8">
<title>Brightmere Picture Works LLC</title>
<link rel="stylesheet" href="https://fonts.googleapis.com/css2?family=Cinzel:wght@400;700&family=PT+Serif:wght@400;700&family=Arimo:wght@400;700&display=swap">
<style>
  :root {
    --bg: #000000;
    --ink: #ffffff;
    --accent: #e27a2c;
    --accent-dim: #b4612a;
    --cream: #f1dfb8;
    --body-text: #e6e6e6;
    --panel: #2a2a2a;
    --panel-edge: #3c3c3c;
    --nav-top: #3a3a3a;
    --nav-bottom: #0c0c0c;
    --nav-line: #555555;
  }
  * { margin: 0; padding: 0; box-sizing: border-box; }
  html, body { width: 1200px; height: 1107px; overflow: hidden; background: var(--bg); }
  body { position: relative; font-family: "PT Serif", Georgia, serif; color: var(--ink); }

  .site-header { position: absolute; left: 0; top: 0; width: 1200px; height: 200px; }
  .brand { position: absolute; left: 48px; top: 50px; display: flex; align-items: center; gap: 14px; }
  .brand-mark { width: 22px; height: 22px; background: var(--ink); }
  .brand-name { font-family: "Cinzel", serif; font-weight: 700; font-size: 30px; color: var(--ink); line-height: 1.05; width: 300px; }
  .reel-art {
    position: absolute; left: 660px; top: 0; width: 540px; height: 200px;
    background: radial-gradient(ellipse at 70% 30%, #6a6a6a 0%, #2c2c2c 45%, #000 80%);
  }
  .search { position: absolute; left: 726px; top: 141px; display: flex; align-items: center; gap: 10px; }
  .search-label { font-family: "Arimo", sans-serif; font-weight: 700; font-size: 19px; color: var(--ink); }
  .search-field { width: 310px; height: 36px; border-radius: 18px; background: #fff; position: relative; }
  .search-field svg { position: absolute; right: 12px; top: 7px; }

  .main-nav {
    position: absolute; left: 60px; top: 210px; width: 1074px; height: 60px;
    display: flex; background: linear-gradient(var(--nav-top), var(--nav-bottom));
    border-top: 1px solid var(--nav-line);
  }
  .main-nav a {
    flex: 1; display: flex; align-items: center; justify-content: center;
    font-family: "Arimo", sans-serif; font-size: 21px; color: var(--ink); text-decoration: none;
    border-right: 2px solid #000; border-left: 1px solid var(--nav-line);
  }
  .main-nav a.current { color: var(--accent); }

  .hero-photo {
    position: absolute; left: 60px; top: 291px; width: 669px; height: 303px;
    background: linear-gradient(#3a0a08 0%, #a3231c 45%, #6d120e 75%, #2a0504 100%);
  }
  .video-still {
    position: absolute; left: 786px; top: 291px; width: 294px; height: 303px;
    background: linear-gradient(135deg, #5b3f8a 0%, #2b2040 50%, #e0a36a 100%);
  }
  .play-button { position: absolute; left: 120px; top: 124px; }

  .content-panel {
    position: absolute; left: 60px; top: 606px; width: 1074px; height: 360px;
    background: linear-gradient(90deg, var(--panel) 0%, #333 60%, var(--panel-edge) 100%);
  }
  .intro { position: absolute; left: 24px; top: 56px; width: 700px; }
  .intro h2 { font-family: "Cinzel", serif; font-weight: 400; font-size: 22px; color: var(--accent); margin-bottom: 8px; }
  .intro h2.history { margin-top: 22px; }
  .intro p { font-size: 15.5px; line-height: 1.4; color: var(--body-text); }
  .more { color: var(--accent); }

  .sidebar { position: absolute; left: 764px; top: 56px; width: 290px; }
  .sidebar h3 { font-family: "Cinzel", serif; font-weight: 400; font-size: 22px; color: var(--accent); line-height: 38px; }
  .sidebar ul { list-style: none; margin-bottom: 7px; }
  .sidebar li { font-family: "PT Serif", serif; font-weight: 700; font-size: 15px; color: var(--cream); line-height: 22px; padding-left: 4px; }

  .site-footer { position: absolute; left: 25px; top: 1004px; width: 1200px; text-align: center; font-family: "Arimo", sans-serif; }
  .footer-links { display: flex; justify-content: center; gap: 36px; font-size: 15px; color: var(--ink); }
  .copyright { margin-top: 24px; font-size: 14px; color: var(--accent-dim); }
</style>
</head>
<body>
  <header class="site-header">
    <div class="reel-art" role="img" aria-label="Film reel and film strip artwork"></div>
    <div class="brand">
      <span class="brand-mark"></span>
      <span class="brand-name">Brightmere Picture Works LLC</span>
    </div>
    <div class="search">
      <span class="search-label">Search</span>
      <div class="search-field">
        <svg width="22" height="22" viewBox="0 0 22 22"><circle cx="9" cy="9" r="6.5" fill="none" stroke="#000" stroke-width="2.5"/><line x1="14" y1="14" x2="20" y2="20" stroke="#000" stroke-width="3" stroke-linecap="round"/></svg>
      </div>
    </div>
  </header>

  <nav class="main-nav">
    <a class="current">Home</a>
    <a>About Us</a>
    <a>Studio</a>
    <a>Movies</a>
    <a>Music Video</a>
    <a>Sign Up</a>
  </nav>

  <div class="hero-photo" role="img" aria-label="Theater auditorium with red seats and a lit stage"></div>
  <div class="video-still" role="img" aria-label="Music video still of a band performing on stage">
    <svg class="play-button" width="56" height="56" viewBox="0 0 56 56"><circle cx="28" cy="28" r="26" fill="#1a1a1a" fill-opacity="0.85" stroke="#fff" stroke-width="2"/><polygon points="22,16 40,28 22,40" fill="#fff"/></svg>
  </div>

  <section class="content-panel">
    <div class="intro">
      <h2>Welcome to our site</h2>
      <p>Our company is a production company that produces films and music videos in Hollywood California for the festivals and theaters around the world.<span class="more">more&gt;&gt;</span></p>
      <h2 class="history">History</h2>
      <p>In 1853, one adobe hut stood in Nopalera, named for the Mexican Nopal cactus indigenous to the area. By 1870, an agricultural community flourished in the area with thriving crops of many common and exotic varieties. The area was known to those residents as the Cahuenga Valley, after the pass in the Santa Monica Mountains immediately to the north. Soon thereafter, land speculation led to subdivision of the large plots and an influx of homeowners. <span class="more">more&gt;&gt;</span></p>
    </div>
    <aside class="sidebar">
      <h3>News</h3>
      <ul>
        <li>Now in Theater</li>
        <li>Upcoming Release</li>
        <li>Top Stories</li>
        <li>Public Review</li>
      </ul>
      <h3>Video Gallery</h3>
      <h3>Photo Gallery</h3>
      <h3>Services</h3>
    </aside>
  </section>

  <footer class="site-footer">
    <div class="footer-links">
      <span>Career</span><span>Corporate Partners</span><span>Privacy Policy</span><span>Terms of Use</span><span>Contact Us</span>
    </div>
    <p class="copyright">Copyright © 2012 Brightmere Picture Works LLC All rights reserved</p>
  </footer>
</body>
</html>
```